Meridian Rest Supply Needs Business Card

Looking for a very nice looking business card. Creative but not extravagant. We sell beds and pillows across the U.S. and need something professional but catchy. I have attached the logo.

Name : Dale Fenwick
Title : President
Phone : (800) 417-2964
Email: sleep@quorvana.com
Website: www.quorvana.com

Can be single-sided or double-sided
horizontal or vertical

Can use Blues/Greys

Target Market(s)

Mass Market

Industry/Entity Type

Retail

Contact Information for Business Card

Name : Dale Fenwick
Title : President
Phone : (800) 417-2964
Email: sleep@quorvana.com
Website: www.quorvana.com

Requirements
Must have
• Clean, Modern, Smooth
• Can use Blues/Greys
• On the other side without the information - have something simple like www.quorvana.com or our logo
Nice to have
• Surprise me
Should not have
• Nothing crazy, nothing cluttered

```html
<!DOCTYPE html>
<html lang="en">
<head>
<meta charset="utf-8">
<title>Quorvana Business Cards</title>
<link href="https://fonts.googleapis.com/css2?family=Montserrat:wght@300;400;500&display=swap" rel="stylesheet">
<style>
  :root {
    --backdrop: #e8e9ea;
    --brand-blue: #29a8df;
    --card-white: #ffffff;
    --card-graphite: #3a3a3c;
    --card-black: #000000;
    --ink-dark: #2b2b2b;
    --ink-light: #ffffff;
  }
  * { box-sizing: border-box; margin: 0; padding: 0; }
  html, body {
    width: 1200px; height: 929px; overflow: hidden;
    background: var(--backdrop);
    font-family: "Montserrat", sans-serif;
  }
  .sheet { position: relative; width: 1200px; height: 929px; }
  .card {
    position: absolute; width: 242px; height: 424px;
    border-radius: 16px; overflow: hidden;
  }
  .card--front-light { left: 344px; top: 27px; background: var(--card-white); color: var(--ink-dark); }
  .card--back-graphite { left: 612px; top: 27px; background: var(--card-graphite); }
  .card--front-dark { left: 344px; top: 473px; background: var(--card-black); color: var(--ink-light); }
  .card--back-dark { left: 612px; top: 473px; background: var(--card-black); }

  .wordmark {
    font-weight: 300; color: var(--brand-blue);
    letter-spacing: 0.01em; line-height: 1;
  }
  .front .wordmark {
    position: absolute; top: 24px; right: 22px; font-size: 32px;
  }
  .back { display: flex; flex-direction: column; align-items: center; justify-content: center; }
  .back .wordmark { font-size: 42px; }
  .back .site {
    margin-top: 12px; font-size: 11px; font-weight: 400;
    letter-spacing: 0.38em; color: var(--ink-light);
    margin-right: -0.38em;
  }

  .accent-tab {
    position: absolute; left: 0; top: 327px; width: 9px; height: 80px;
    background: var(--brand-blue); border-radius: 0 5px 5px 0;
  }
  .contact { position: absolute; left: 23px; top: 325px; }
  .contact .name { font-size: 17px; font-weight: 500; color: var(--brand-blue); line-height: 1.1; }
  .contact .title { font-size: 10.5px; font-weight: 400; margin-top: 1px; }
  .contact .lines { list-style: none; margin-top: 9px; }
  .contact .lines li {
    display: flex; align-items: center; gap: 5px;
    font-size: 10.5px; line-height: 13.3px;
  }
  .contact svg { width: 7px; height: 7px; flex: none; }
  .contact svg * { fill: none; stroke: var(--brand-blue); stroke-width: 1.2; }
  .contact svg .solid { fill: var(--brand-blue); stroke: none; }
</style>
</head>
<body>
<main class="sheet">

  <section class="card card--front-light front">
    <div class="wordmark">quorvana</div>
    <div class="accent-tab"></div>
    <div class="contact">
      <p class="name">Dale Fenwick</p>
      <p class="title">President</p>
      <ul class="lines">
        <li><svg viewBox="0 0 10 10"><path class="solid" d="M2 0.5 L4 2.8 L3 4 Q4.5 6.5 6 7 L7.2 6 L9.5 8 L8 9.6 Q3 9 0.5 2 Z"/></svg>(800) 417-2964</li>
        <li><svg viewBox="0 0 10 10"><rect x="0.8" y="2" width="8.4" height="6"/><path d="M0.8 2 L5 5.5 L9.2 2"/></svg>sleep@quorvana.com</li>
        <li><svg viewBox="0 0 10 10"><circle cx="5" cy="5" r="4.2"/><ellipse cx="5" cy="5" rx="1.8" ry="4.2"/><path d="M0.8 5 H9.2"/></svg>www.quorvana.com</li>
      </ul>
    </div>
  </section>

  <section class="card card--back-graphite back">
    <div class="wordmark">quorvana</div>
    <p class="site">www.quorvana.com</p>
  </section>

  <section class="card card--front-dark front">
    <div class="wordmark">quorvana</div>
    <div class="accent-tab"></div>
    <div class="contact">
      <p class="name">Dale Fenwick</p>
      <p class="title">President</p>
      <ul class="lines">
        <li><svg viewBox="0 0 10 10"><path class="solid" d="M2 0.5 L4 2.8 L3 4 Q4.5 6.5 6 7 L7.2 6 L9.5 8 L8 9.6 Q3 9 0.5 2 Z"/></svg>(800) 417-2964</li>
        <li><svg viewBox="0 0 10 10"><rect x="0.8" y="2" width="8.4" height="6"/><path d="M0.8 2 L5 5.5 L9.2 2"/></svg>sleep@quorvana.com</li>
        <li><svg viewBox="0 0 10 10"><circle cx="5" cy="5" r="4.2"/><ellipse cx="5" cy="5" rx="1.8" ry="4.2"/><path d="M0.8 5 H9.2"/></svg>www.quorvana.com</li>
      </ul>
    </div>
  </section>

  <section class="card card--back-dark back">
    <div class="wordmark">quorvana</div>
    <p class="site">www.quorvana.com</p>
  </section>

</main>
</body>
</html>
```